Beautiful Customer Appreciation Gift Box Need Eye Catching Brochure

I need a brochure to include with small sample gift boxes that I send or give to companies who do door to door marketing of businesses, company reps, real estate designers and large companies looking for a unique customer appreciation gifts.

The brochure needs to capture the size variations and the limitless options for their budget and customization needs.

They are gift boxes that can be filled with cookies for the drug rep making an impression for the doc - after cookies are gone, the gift remains

At christmas, we fill them with baked goods and provide to each office. Every year as i visit the offices, they have last years gift box out as a decoration.

realtors can use them as a welcome to your new home gift filled with a bottle of wine and their papers left on the kitchen counter

We have had them used for baby shower gifts, kept later as a decoration.

that's the concept, i need it captured.
Marlow's Festive Nook is the current name
a tag line we came up with is It's all in the WRAPPINGS.
Updates

Project Deadline Extended
Reason: We are very close, I have my photoshoot tomorrow and I'd like to see and continue to tweek the current designs. I have pretty well deleted the designs we are not considering at this point. The others all have components we love. So I need a little more time and some tweaking to decide for sure.

Target Market(s)

the target is the company or individuals looking for gift giving options for clients and customers. From the door to door salesperson looking to make a splash or big impression to the large company looking for nice corporate gift ideas.

The concept of say goodbye to plain jane gift boxes that all look alike... Say goodbye to expensive gift wrap and bows that get thrown away in minutes.... and hello to a beautiful custom made gift box that will remain a decoration or keepsake box forever....

Industry/Entity Type

Retail

Font styles to use
Sans Serif
Script

Requirements
Must have
• IMPORTANT... I CAN and AM GETTING better pictures for the printing purposes. I'm looking more for the concept of the brochuure and layout design.
• I'd love to have it have some place holders for various pictures and descriptions - because each industry targets different people, I'd like to be able to change the front cover of the brochure with a picture of a box that targets that audience a little.
• For a real estate person... i might choose a beautiful centerpiece looking one... vs, the ob/gyn office, I might choose a baby one.
• I have some design skill, just 0 times and the programs have changed alot over the years, so this may go on to future work and a long design relationship as the company grows and changes. I do know photoshop and pagemaker from long ago so I should be able to drop in pics and text options. if we use compatible programs.
Nice to have
• would love to have some kind of background for the page - not just plain white background.
• i like angles and curves
Should not have
• boxy look.

```html
<!DOCTYPE html>
<html lang="en">
<head>
<meta charset="utf-8">
<title>Gift Box Collection Brochure Spread</title>
<link href="https://fonts.googleapis.com/css2?family=Gelasio:wght@400;700&family=Italianno&display=swap" rel="stylesheet">
<style>
:root{
  --backdrop:#d5d6d8;
  --paper:#ffffff;
  --teal:#4c97a1;
  --ink:#5a5a5a;
  --gold:#d5b16c;
  --fold:#ececec;
}
*{margin:0;padding:0;box-sizing:border-box}
html,body{width:1200px;height:1000px;overflow:hidden;background:var(--backdrop)}
.spread{position:absolute;left:84px;top:101px;width:1031px;height:796px;background:var(--paper);box-shadow:0 4px 14px rgba(0,0,0,.35)}
.spread::after{content:"";position:absolute;left:515px;top:0;width:1px;height:100%;background:var(--fold)}
.headline{position:absolute;left:0;right:0;top:40px;text-align:center;font-family:"Gelasio",serif;font-weight:400;font-size:19px;color:var(--ink);letter-spacing:.3px}
.headline strong{color:var(--teal);font-weight:700}
.rule{position:absolute;left:28px;width:975px;height:2px;background:var(--teal)}
.rule--top{top:89px}
.rule--bottom{top:760px}
.product-photo{position:absolute;width:227px;height:144px;display:flex}
.product-photo span{flex:1}
.product-info{position:absolute;width:240px}
.product-name{font-family:"Italianno",cursive;font-weight:400;font-size:31px;color:var(--teal);line-height:1;height:28px;white-space:nowrap}
.product-text{font-family:"Gelasio",serif;font-size:14.5px;color:var(--ink);line-height:19px;margin-left:9px;margin-top:3px;white-space:nowrap}
.price{font-family:"Gelasio",serif;font-size:14.5px;color:var(--ink);margin-left:9px;margin-top:15px;display:flex;align-items:center;gap:6px}
.stars{display:flex;gap:0}
.stars svg{width:25px;height:25px}
.star-full{fill:var(--gold);stroke:var(--gold);stroke-width:1}
.star-empty{fill:none;stroke:var(--gold);stroke-width:1.2}
.tone-baby span:first-child{background:linear-gradient(160deg,#6f7d54,#d98fb8 45%,#c5c4e6)}
.tone-baby span:last-child{background:linear-gradient(160deg,#8a6a78,#e9b4d6 50%,#c8b6de)}
.tone-book span:first-child{background:linear-gradient(160deg,#5a4a3c,#6f8a3e 45%,#a58f66)}
.tone-book span:last-child{background:linear-gradient(160deg,#6a8a3a,#3a2f2a 55%,#e3d3a3)}
.tone-pink span:first-child{background:linear-gradient(160deg,#4b3a2e,#e8b5c4 45%,#d99fb5)}
.tone-pink span:last-child{background:linear-gradient(160deg,#6b5a4a,#e3a3bd 45%,#c78aa3)}
.tone-paris span:first-child{background:linear-gradient(160deg,#6b5a4a,#7d5fb8 45%,#4a3a2a)}
.tone-paris span:last-child{background:linear-gradient(160deg,#5d7a3a,#3a2f6a 50%,#8b6a3a)}
</style>
</head>
<body>
<svg width="0" height="0" style="position:absolute">
  <defs>
    <path id="star" d="M12 1.5l3.1 6.6 7.2.9-5.3 5 1.4 7.1L12 17.6l-6.4 3.5 1.4-7.1-5.3-5 7.2-.9z"/>
  </defs>
</svg>

<main class="spread">
  <h1 class="headline"><strong>LIMITLESS</strong> OPTIONS&nbsp; FOR YOUR BUDGET AND <strong>CUSTOMIZATION</strong> NEEDS.</h1>
  <div class="rule rule--top"></div>

  <div class="product-photo tone-baby" style="left:29px;top:113px" role="img" aria-label="Flower arrangement in an alphabet baby gift box with a plush toy"><span></span><span></span></div>
  <div class="product-info" style="left:268px;top:131px"><h2 class="product-name">Alphabet Garden</h2><p class="product-text">Lorem ipsum dolor sit amet.<br>Lorem ipsum dolor sit amet.</p><div class="price">Price :<span class="stars"><svg viewBox="0 0 24 24"><use href="#star" class="star-full"/></svg><svg viewBox="0 0 24 24"><use href="#star" class="star-empty"/></svg><svg viewBox="0 0 24 24"><use href="#star" class="star-empty"/></svg><svg viewBox="0 0 24 24"><use href="#star" class="star-empty"/></svg><svg viewBox="0 0 24 24"><use href="#star" class="star-empty"/></svg></span></div></div>

  <div class="product-info" style="left:28px;top:292px"><h2 class="product-name">Storybook Bloom</h2><p class="product-text">Lorem ipsum dolor sit amet.<br>Lorem ipsum dolor sit amet.</p><div class="price">Price :<span class="stars"><svg viewBox="0 0 24 24"><use href="#star" class="star-full"/></svg><svg viewBox="0 0 24 24"><use href="#star" class="star-full"/></svg><svg viewBox="0 0 24 24"><use href="#star" class="star-full"/></svg><svg viewBox="0 0 24 24"><use href="#star" class="star-full"/></svg><svg viewBox="0 0 24 24"><use href="#star" class="star-full"/></svg></span></div></div>
  <div class="product-photo tone-book" style="left:259px;top:274px" role="img" aria-label="Green floral arrangement on a book-shaped keepsake box"><span></span><span></span></div>

  <div class="product-photo tone-pink" style="left:29px;top:435px" role="img" aria-label="Pink roses in a vintage French shop gift box"><span></span><span></span></div>
  <div class="product-info" style="left:268px;top:453px"><h2 class="product-name">Maison De Fleurs</h2><p class="product-text">Lorem ipsum dolor sit amet.<br>Lorem ipsum dolor sit amet.</p><div class="price">Price :<span class="stars"><svg viewBox="0 0 24 24"><use href="#star" class="star-full"/></svg><svg viewBox="0 0 24 24"><use href="#star" class="star-full"/></svg><svg viewBox="0 0 24 24"><use href="#star" class="star-full"/></svg><svg viewBox="0 0 24 24"><use href="#star" class="star-full"/></svg><svg viewBox="0 0 24 24"><use href="#star" class="star-full"/></svg></span></div></div>

  <div class="product-info" style="left:28px;top:614px"><h2 class="product-name">Violette De Paris</h2><p class="product-text">Lorem ipsum dolor sit amet.<br>Lorem ipsum dolor sit amet.</p><div class="price">Price :<span class="stars"><svg viewBox="0 0 24 24"><use href="#star" class="star-full"/></svg><svg viewBox="0 0 24 24"><use href="#star" class="star-full"/></svg><svg viewBox="0 0 24 24"><use href="#star" class="star-full"/></svg><svg viewBox="0 0 24 24"><use href="#star" class="star-full"/></svg><svg viewBox="0 0 24 24"><use href="#star" class="star-empty"/></svg></span></div></div>
  <div class="product-photo tone-paris" style="left:259px;top:596px" role="img" aria-label="Purple flowers on a Paris-themed book box filled with treats"><span></span><span></span></div>

  <div class="product-photo tone-baby" style="left:546px;top:113px" role="img" aria-label="Flower arrangement in an alphabet baby gift box with a plush toy"><span></span><span></span></div>
  <div class="product-info" style="left:785px;top:131px"><h2 class="product-name">Alphabet Garden</h2><p class="product-text">Lorem ipsum dolor sit amet.<br>Lorem ipsum dolor sit amet.</p><div class="price">Price :<span class="stars"><svg viewBox="0 0 24 24"><use href="#star" class="star-full"/></svg><svg viewBox="0 0 24 24"><use href="#star" class="star-empty"/></svg><svg viewBox="0 0 24 24"><use href="#star" class="star-empty"/></svg><svg viewBox="0 0 24 24"><use href="#star" class="star-empty"/></svg><svg viewBox="0 0 24 24"><use href="#star" class="star-empty"/></svg></span></div></div>

  <div class="product-info" style="left:544px;top:292px"><h2 class="product-name">Storybook Bloom</h2><p class="product-text">Lorem ipsum dolor sit amet.<br>Lorem ipsum dolor sit amet.</p><div class="price">Price :<span class="stars"><svg viewBox="0 0 24 24"><use href="#star" class="star-full"/></svg><svg viewBox="0 0 24 24"><use href="#star" class="star-full"/></svg><svg viewBox="0 0 24 24"><use href="#star" class="star-full"/></svg><svg viewBox="0 0 24 24"><use href="#star" class="star-full"/></svg><svg viewBox="0 0 24 24"><use href="#star" class="star-full"/></svg></span></div></div>
  <div class="product-photo tone-book" style="left:775px;top:274px" role="img" aria-label="Green floral arrangement on a book-shaped keepsake box"><span></span><span></span></div>

  <div class="product-photo tone-pink" style="left:546px;top:435px" role="img" aria-label="Pink roses in a vintage French shop gift box"><span></span><span></span></div>
  <div class="product-info" style="left:785px;top:453px"><h2 class="product-name">Maison De Fleurs</h2><p class="product-text">Lorem ipsum dolor sit amet.<br>Lorem ipsum dolor sit amet.</p><div class="price">Price :<span class="stars"><svg viewBox="0 0 24 24"><use href="#star" class="star-full"/></svg><svg viewBox="0 0 24 24"><use href="#star" class="star-full"/></svg><svg viewBox="0 0 24 24"><use href="#star" class="star-full"/></svg><svg viewBox="0 0 24 24"><use href="#star" class="star-full"/></svg><svg viewBox="0 0 24 24"><use href="#star" class="star-full"/></svg></span></div></div>

  <div class="product-info" style="left:544px;top:614px"><h2 class="product-name">Violette De Paris</h2><p class="product-text">Lorem ipsum dolor sit amet.<br>Lorem ipsum dolor sit amet.</p><div class="price">Price :<span class="stars"><svg viewBox="0 0 24 24"><use href="#star" class="star-full"/></svg><svg viewBox="0 0 24 24"><use href="#star" class="star-full"/></svg><svg viewBox="0 0 24 24"><use href="#star" class="star-full"/></svg><svg viewBox="0 0 24 24"><use href="#star" class="star-full"/></svg><svg viewBox="0 0 24 24"><use href="#star" class="star-empty"/></svg></span></div></div>
  <div class="product-photo tone-paris" style="left:775px;top:596px" role="img" aria-label="Purple flowers on a Paris-themed book box filled with treats"><span></span><span></span></div>

  <div class="rule rule--bottom"></div>
</main>
</body>
</html>
```